BUSINESS CARD - HALVERDINE RURAL SERVICES

I would like to create a business card for my fertilizer spreading business. I would like to incorporate my existing logo and also a description of the services offered. The business card will be given to farmers so must be kept simple but effective. It will also be left in stores so much also be eye catching in order to stand out from other cards.

Target Market(s)

FARMERS

Requirements
Must have
• FRONT OF CARD = EXISTING LOGO + "CUSTOMISED SPREADING" below the logo

REAR Of CARD = SERVICES OFFERED AND CONTACT DETAILS

- Bulk fertilizer including Lime, Gypsum, Manure & Compost
- Granular fertilizer including Single Super, Urea, Granfeed, & Custom Blends
- Modern equipment - Autosteer & Variable Rate Capable
- Friendly & Reliable Service
- Contact Gus: 0471 502 318
Nice to have
• utilize same color scheme as existing logo

```html
<!DOCTYPE html>
<html lang="en">
<head>
<meta charset="utf-8">
<title>Halverdine Rural Services – Business Card</title>
<link href="https://fonts.googleapis.com/css2?family=Poppins:wght@400;500;600;700&display=swap" rel="stylesheet">
<style>
  :root {
    --orange: #f58220;
    --orange-deep: #ee6a12;
    --orange-light: #f8a13a;
    --ink: #1d1d1d;
    --grey: #5a5a5a;
    --paper: #ffffff;
    --paper-shade: #e6e6e6;
    --backdrop: #2b2d31;
  }
  * { box-sizing: border-box; margin: 0; padding: 0; }
  html, body { width: 1200px; height: 900px; overflow: hidden; }
  body {
    background: var(--backdrop);
    font-family: "Poppins", sans-serif;
    position: relative;
  }
  .card {
    position: absolute;
    top: 295px;
    width: 540px;
    height: 310px;
    border-radius: 22px;
    overflow: hidden;
  }

  /* ---------- Rear ---------- */
  .card-rear {
    left: 30px;
    background: linear-gradient(160deg, var(--paper) 0%, #f4f4f4 45%, var(--paper-shade) 100%);
  }
  .rear-edge-top {
    position: absolute; top: 0; right: 0; width: 62%; height: 7px;
    background: var(--orange);
  }
  .rear-edge-left {
    position: absolute; bottom: 0; left: 0; width: 7px; height: 62%;
    background: var(--orange);
  }
  .rear-brand {
    position: absolute; top: 22px; left: 26px;
    display: flex; align-items: center; gap: 12px;
  }
  .brand-dot {
    width: 44px; height: 44px; border-radius: 50%;
    background: var(--grey);
    flex: none;
  }
  .rear-brand .brand-name {
    font-weight: 700; font-size: 22px; line-height: 1.05;
    color: var(--ink); letter-spacing: -0.5px;
  }
  .rear-brand .brand-name span { display: block; font-size: 12px; letter-spacing: 4px; }
  .brand-rule {
    position: absolute; top: 80px; left: 82px; width: 190px; height: 2px;
    background: var(--orange);
  }
  .services {
    position: absolute; top: 100px; left: 26px; width: 490px;
    list-style: none;
    font-size: 11.5px; font-weight: 500; color: var(--ink); line-height: 1.9;
  }
  .services li::before {
    content: ""; display: inline-block; width: 6px; height: 6px;
    background: var(--ink); transform: rotate(45deg);
    margin-right: 8px; vertical-align: middle;
  }
  .services .hl { color: var(--orange); font-weight: 600; }
  .contact {
    position: absolute; top: 180px; right: 30px; text-align: right;
    border-right: 3px solid var(--ink); padding-right: 12px;
  }
  .contact-label { font-size: 16px; font-weight: 600; color: var(--ink); }
  .contact-label .hl { color: var(--orange); }
  .contact-phone { font-size: 28px; font-weight: 600; color: var(--orange); line-height: 1.1; }
  .tagline {
    position: absolute; bottom: 0; left: 150px; right: 0; height: 42px;
    background: var(--ink);
    clip-path: polygon(22px 0, 100% 0, 100% 100%, 0 100%);
    color: var(--paper); font-size: 15px; font-weight: 500;
    display: flex; align-items: center; padding-left: 48px;
  }
  .tagline .hl { color: var(--orange); margin-right: 5px; }

  /* ---------- Front ---------- */
  .card-front {
    left: 630px;
    background: radial-gradient(circle at 30% 70%, var(--orange-light) 0%, var(--orange) 45%, var(--orange-deep) 100%);
  }
  .front-texture {
    position: absolute; inset: 0;
    background: linear-gradient(135deg, rgba(255,255,255,0.06), rgba(0,0,0,0.04));
  }
  .front-brand {
    position: absolute; top: 58px; left: 0; right: 0;
    display: flex; flex-direction: column; align-items: center; gap: 10px;
  }
  .front-brand .brand-dot { width: 70px; height: 70px; background: var(--paper); }
  .front-brand .brand-name {
    font-weight: 700; font-size: 34px; color: var(--paper);
    letter-spacing: -0.5px; line-height: 1.05; text-align: center;
  }
  .front-brand .brand-name span { display: block; font-size: 14px; letter-spacing: 6px; }
  .front-band {
    position: absolute; top: 224px; left: 0; width: 320px; height: 40px;
    background: var(--paper);
    display: flex; align-items: center; padding-left: 26px;
    color: var(--orange); font-size: 19px; font-weight: 600;
  }
  .band-slashes { position: absolute; top: 224px; left: 326px; }
</style>
</head>
<body>

<section class="card card-rear" aria-label="Card rear">
  <div class="rear-edge-top"></div>
  <div class="rear-edge-left"></div>
  <div class="rear-brand">
    <div class="brand-dot"></div>
    <div class="brand-name">Halverdine Rural<span>SERVICES</span></div>
  </div>
  <div class="brand-rule"></div>
  <ul class="services">
    <li><span class="hl">Bulk fertilizer</span> including Lime, Gypsum, Manure &amp; Compost</li>
    <li><span class="hl">Granular fertilizer</span> including Single Super, Urea, Granfeed, &amp; Custom Blends</li>
    <li><span class="hl">Modern equipment</span> - Autosteer &amp; Variable Rate Capable</li>
  </ul>
  <div class="contact">
    <div class="contact-label">Contact <span class="hl">Gus</span></div>
    <div class="contact-phone">0471 502 318</div>
  </div>
  <div class="tagline"><span class="hl">Friendly</span> &amp; Reliable Service</div>
</section>

<section class="card card-front" aria-label="Card front">
  <div class="front-texture" role="img" aria-label="Subtle orange lattice pattern background"></div>
  <div class="front-brand">
    <div class="brand-dot"></div>
    <div class="brand-name">Halverdine Rural<span>SERVICES</span></div>
  </div>
  <div class="front-band">Customised Spreading</div>
  <svg class="band-slashes" width="40" height="40" viewBox="0 0 40 40">
    <line x1="12" y1="2" x2="4" y2="38" stroke="#fff" stroke-width="3"/>
    <line x1="22" y1="2" x2="14" y2="38" stroke="#fff" stroke-width="3"/>
    <line x1="32" y1="2" x2="24" y2="38" stroke="#fff" stroke-width="3"/>
  </svg>
</section>

</body>
</html>
```